Poetry Book Cover Design Project

Looking for a minimalistic book cover design for a collection of poems. The book title is "Before The Morning Turns To Glass". There are three parts to the book. First covers poetry in the theme of Rage. Second love and desire. The third is strange poems. Essentially the sections are "Rage", "Desire" and the "Strange". The reason for the title "Before The Morning Turns To Glass" is as if someone is writing these till life changes towards the intended outcome as felt in each poem. I want to have the author's name "Nirosha Kulathunge" at the bottom. Ilustration attached.
- Minimalistic

```html
<!DOCTYPE html>
<html lang="en">
<head>
<meta charset="utf-8">
<title>Before The Morning Turns To Glass — Nirosha Kulathunge</title>
<link rel="stylesheet" href="https://fonts.googleapis.com/css2?family=Crimson+Pro:wght@400&display=swap">
<style>
  :root {
    --paper: #ffffff;
    --title-red: #df0f22;
    --ink: #222222;
    --artwork-tone: #f0f0f0;
  }
  * { margin: 0; padding: 0; box-sizing: border-box; }
  html, body {
    width: 800px;
    height: 1200px;
    overflow: hidden;
    background: var(--paper);
  }
  .cover {
    position: relative;
    width: 800px;
    height: 1200px;
    background: var(--paper);
  }
  .cover-artwork {
    position: absolute;
    left: 18px;
    top: 58px;
    width: 500px;
    height: 686px;
  }
  .book-title {
    position: absolute;
    right: 46px;
    top: 178px;
    text-align: right;
    font-family: "Crimson Pro", Georgia, serif;
    font-weight: 400;
    font-size: 150px;
    line-height: 142px;
    letter-spacing: -0.02em;
    color: var(--title-red);
  }
  .book-title .title-line { display: block; }
  .author-name {
    position: absolute;
    left: 0;
    right: 0;
    top: 1090px;
    text-align: center;
    font-family: "Crimson Pro", Georgia, serif;
    font-weight: 400;
    font-size: 38px;
    letter-spacing: 0.14em;
    color: var(--ink);
  }
</style>
</head>
<body>
  <main class="cover">
    <svg class="cover-artwork" viewBox="0 0 500 686" role="img" aria-label="Continuous single-line drawing of several overlapping abstract faces in black ink">
      <rect x="0" y="0" width="500" height="686" rx="40" fill="var(--artwork-tone)"/>
    </svg>
    <h1 class="book-title">
      <span class="title-line">Before</span>
      <span class="title-line">The</span>
      <span class="title-line">Morning</span>
      <span class="title-line">Turns</span>
      <span class="title-line">To</span>
      <span class="title-line">Glass</span>
    </h1>
    <p class="author-name">Nirosha Kulathunge</p>
  </main>
</body>
</html>
```